Home Security and Smart Home Flyer

A professional flyer to Hand out to people to get them interested in our service, also have a special promotion on it. Have our product on it. We are a home security company and our goal is to get as many clients as possible with great deals to protect we also provide smart home automation products

Target Market(s)

Anyone Owns a home. Anyone that currently has the old alarm

Industry/Entity Type

Security Service

Font styles to use
Sans Serif

Colors
33a6d7
ec1f27
0255a3
ffffff
0393ce
85cae6
cee9f5
3276b5
85acd3

Requirements
Must have
• The alarm panel, doorbell camera. Our monthly rate starting as low as 29.99. Free Sameday installation, Free Equipment. Our Brightfort Guard logo. And brightfort guard on anything that has to do with the company. Phone number 8005551643. Website www.brightfortguardhq.com. Needs to be double sided.
• Free Doorbell Camera
• Free Installation
• Free Smart Home Security System
• Arizona Preferred Choice
• Award-winning service
• Best deal out there guaranteed
• “You find someone out there better will beat it”
Nice to have
• Imagine you on your home and you were wanting me to get a really cool system in your home watch with me you shoes instead of other people design the flyer around that make it look really interesting so they want to call back with the great offers were already presented to them
Should not have
• Do not have anything that says Qmx on it or Sorbel on it.

```html
<!DOCTYPE html>
<html lang="en">
<head>
<meta charset="utf-8">
<title>Brightfort Guard – Home Security Flyer</title>
<link rel="stylesheet" href="https://fonts.googleapis.com/css2?family=Open+Sans:wght@300;400;600;700;800&display=swap">
<style>
  :root {
    --sky: #2fa9dc;
    --sky-deep: #0393ce;
    --navy: #0d4462;
    --band-dark: #0a4566;
    --band-light: #1c6688;
    --ink: #5d5f61;
    --ink-dark: #3f4143;
    --grey-band: #dcdfe0;
    --white: #ffffff;
    --stage: #2a2a2a;
  }
  * { margin: 0; padding: 0; box-sizing: border-box; }
  html, body { width: 1200px; height: 960px; overflow: hidden; }
  body { background: var(--stage); font-family: "Open Sans", sans-serif; }

  .flyer {
    position: absolute; left: 0; top: 55px;
    width: 1200px; height: 850px;
    background: var(--white); overflow: hidden;
  }
  .flyer > * { position: absolute; }

  .accent-shape { left: 0; top: 0; width: 1200px; height: 850px; }

  .brand-name {
    left: 58px; top: 62px;
    font-weight: 400; font-size: 44px; line-height: 48px;
    letter-spacing: 7px; color: var(--navy);
  }
  .headline {
    left: 423px; top: 44px;
    font-weight: 400; font-size: 53px; line-height: 61px;
    color: var(--navy);
  }

  .intro-band {
    left: 0; top: 188px; width: 980px; height: 94px;
    background: linear-gradient(170deg, var(--band-light) 0%, var(--band-dark) 45%, var(--band-dark) 100%);
  }
  .intro-text {
    left: 59px; top: 198px;
    font-weight: 300; font-size: 28px; line-height: 38px;
    color: var(--white);
  }

  .rate-label {
    left: 58px; top: 318px;
    font-weight: 600; font-size: 39px; line-height: 46px;
    color: var(--ink);
  }
  .rate-price {
    left: 486px; top: 290px;
    font-weight: 800; font-size: 128px; line-height: 140px;
    letter-spacing: -3px; color: var(--sky);
  }

  .offer-band { left: 0; top: 449px; width: 840px; height: 128px; background: var(--grey-band); }
  .offer-free {
    left: 38px; top: 440px;
    font-weight: 800; font-size: 112px; line-height: 140px;
    letter-spacing: -2px; color: var(--sky);
  }
  .offer-items {
    left: 298px; top: 470px;
    font-weight: 600; font-size: 34px; line-height: 43px;
    color: var(--ink);
  }

  .tagline { left: 43px; top: 592px; font-size: 21px; color: var(--ink); }

  .contact-title {
    left: 43px; top: 655px; width: 526px;
    padding-bottom: 2px; border-bottom: 2px solid var(--sky-deep);
    font-weight: 400; font-size: 33px; line-height: 40px;
    color: var(--sky-deep);
  }
  .contact-list { left: 43px; top: 713px; list-style: none; }
  .contact-list li {
    display: flex; align-items: center; gap: 14px;
    font-weight: 400; font-size: 34px; line-height: 44px;
    color: var(--ink-dark);
  }
  .contact-list svg { width: 30px; height: 30px; flex: none; }

  .priority {
    right: 20px; top: 320px; text-align: right;
    font-weight: 300; color: var(--white);
    font-size: 27px; line-height: 29px;
  }
  .priority strong { display: block; font-weight: 400; font-size: 33px; line-height: 40px; }

  .feature-icon { width: 100px; height: 100px; }
  .feature-icon.is-camera { left: 877px; top: 270px; }
  .feature-icon.is-report { left: 977px; top: 200px; }
  .feature-icon.is-idea { left: 1078px; top: 132px; }

  .product-panel { left: 714px; top: 427px; width: 470px; height: 385px; }
  .product-doorbell { left: 590px; top: 590px; width: 232px; height: 232px; }
</style>
</head>
<body>
<main class="flyer">
  <svg class="accent-shape" viewBox="0 0 1200 850" aria-hidden="true">
    <rect class="band-placeholder" x="0" y="0" width="0" height="0"/>
  </svg>

  <div class="intro-band"></div>

  <svg class="accent-shape" viewBox="0 0 1200 850" aria-hidden="true">
    <polygon points="1200,33 853,270 853,850 1200,850" fill="var(--sky)"/>
  </svg>

  <div class="brand-name">BRIGHTFORT<br>GUARD</div>

  <h1 class="headline">FEEL SECURE &amp; SAFE WITH<br>BRIGHTFORT GUARD</h1>

  <p class="intro-text">KEEP YOUR FAMILY SAFE AND SECURE WITH THE INDUSTRY'S<br>LEADING ALARM AND MONITORING SYSTEMS.</p>

  <p class="rate-label">OUR MONTHLY RATE<br>STARTING AS LOW AS</p>
  <p class="rate-price">29.99</p>

  <div class="offer-band"></div>
  <p class="offer-free">FREE</p>
  <p class="offer-items">SAMEDAY INSTALLATION<br>EQUIPMENT</p>

  <p class="tagline">Brightfort guard on anything that has to do with the company.</p>

  <h2 class="contact-title">GET IN TOUCH WITH US!</h2>
  <ul class="contact-list">
    <li>
      <svg viewBox="0 0 30 30" aria-hidden="true">
        <path d="M3 11c0-4 6-6 12-6s12 2 12 6v2h-6v-3c-2-1-10-1-12 0v3H3z" fill="var(--navy)"/>
        <path d="M8 14h14l3 10H5z" fill="var(--navy)"/>
      </svg>
      <span>8005551643</span>
    </li>
    <li>
      <svg viewBox="0 0 30 30" aria-hidden="true" fill="none" stroke="var(--navy)" stroke-width="2">
        <circle cx="15" cy="15" r="11"/>
        <ellipse cx="15" cy="15" rx="5" ry="11"/>
        <line x1="4" y1="15" x2="26" y2="15"/>
        <line x1="6" y1="9" x2="24" y2="9"/>
        <line x1="6" y1="21" x2="24" y2="21"/>
      </svg>
      <span>www.brightfortguardhq.com</span>
    </li>
  </ul>

  <svg class="feature-icon is-camera" viewBox="0 0 100 100" role="img" aria-label="Security camera icon">
    <circle cx="50" cy="50" r="48" fill="var(--white)"/>
    <circle cx="50" cy="50" r="41" fill="none" stroke="var(--sky)" stroke-width="2"/>
  </svg>
  <svg class="feature-icon is-report" viewBox="0 0 100 100" role="img" aria-label="Monitoring report icon">
    <circle cx="50" cy="50" r="48" fill="var(--white)"/>
    <circle cx="50" cy="50" r="41" fill="none" stroke="var(--sky)" stroke-width="2"/>
  </svg>
  <svg class="feature-icon is-idea" viewBox="0 0 100 100" role="img" aria-label="Smart home idea icon">
    <circle cx="50" cy="50" r="48" fill="var(--white)"/>
    <circle cx="50" cy="50" r="41" fill="none" stroke="var(--sky)" stroke-width="2"/>
  </svg>

  <p class="priority">YOUR<br>PROTECTION IS<strong>OUR PRIORITY</strong></p>

  <svg class="product-panel" viewBox="0 0 470 385" role="img" aria-label="Photo of the white smart alarm panel">
    <defs>
      <linearGradient id="panelTone" x1="0" y1="0" x2="1" y2="1">
        <stop offset="0" stop-color="#f4f5f6"/>
        <stop offset="1" stop-color="#d9dcde"/>
      </linearGradient>
    </defs>
    <rect x="2" y="2" width="462" height="378" rx="26" fill="url(#panelTone)"/>
  </svg>

  <svg class="product-doorbell" viewBox="0 0 232 232" role="img" aria-label="Photo of the round doorbell camera">
    <defs>
      <radialGradient id="doorbellTone" cx="0.4" cy="0.35" r="0.7">
        <stop offset="0" stop-color="#f1f1f1"/>
        <stop offset="1" stop-color="#c4c6c8"/>
      </radialGradient>
    </defs>
    <circle cx="116" cy="116" r="113" fill="url(#doorbellTone)"/>
  </svg>
</main>
</body>
</html>
```